Trendy Stylish Safety/Sports glasses polybag and box packaging

Polybag artwork required for safety glasses.
Polybag artwork required for sports glasses.
Packing box artwork required to tie in with polybag packaging.

Both bags to be similar, however one for safety glasses and one for sports glasses.
Maybe touch of different colours to differentiate.

Polybag Packaging for safety glasses.
1. Text to be white on black or vice versa, with a touch of yellow
2. Kermo logos to use, attached.
3. Front of bag to have clear vision panel on RH side
4. Bullet points can be on this clear vision panel.
5. Strapline to be on front of bag after ‘kerMosafety’ is COMFORT…STYLE…PROTECTION
6. Happy to have a touch of other colours on the packet to brighten up, make distinctive.
7. RH side at top on reverse of bag, bar code label to be attached, so this section to be left clear
8. Could have a few safety symbols on possibly.
9. Full text required on polybag is in file ‘safety packaging bag info.docx’

Polybag packaging for sports glasses

1. Text to be white on black or vice versa, with a touch of blue
5. Strapline to be on front of bag after ‘kerMosports’ is PERFORMANCE.…STYLE…PROTECTION
8. Full text required on polybag is in file ‘SPORTS packaging BAG Details.docx’
We havent decided on text for the reverse of this bag, however once we have the basic layout, we can add text at a later stage.

Cardboard packing/posting box for case.

We will use these boxes to pack and despatch our sports and safety glasses.

1. Two long sides of box to match polybag kerMo safety design.
Text required on safety sides of box
kerMosafety logo
COMFORT, STYLE, PROTECTION
2. Two long sides of box to match polybag kerMo sports design.
3. Text required on sports sides of box
kerMosports logo
PERFORMANCE, STYLE, PROTECTION
4. case box jpg has sizes required
Example of packing box picture attached.

Industry/Entity Type

Safety

```html
<!DOCTYPE html>
<html lang="en">
<head>
<meta charset="utf-8">
<title>kerMosafety – Safety Eyewear Polybag Reverse</title>
<link rel="stylesheet" href="https://fonts.googleapis.com/css2?family=Didact+Gothic&display=swap">
<style>
  :root {
    --ink: #0b0b0b;
    --paper: #ffffff;
    --accent: #f7dc00;
    --text: #1a1a1a;
    --rule: #111111;
    --silver-light: #f3f3f3;
    --silver-dark: #bdbdbd;
  }
  * { box-sizing: border-box; margin: 0; padding: 0; }
  html, body {
    width: 1200px; height: 1200px; overflow: hidden;
    background: var(--paper);
    font-family: "Didact Gothic", "Century Gothic", Arial, sans-serif;
  }
  .canvas { position: relative; width: 1200px; height: 1200px; }

  .bag {
    position: absolute; left: 398px; top: 62px;
    width: 408px; height: 1074px;
    background: var(--ink);
    border: 1px solid var(--ink);
    overflow: hidden;
  }
  .header { position: absolute; left: 0; top: 0; width: 100%; height: 186px; border-bottom: 1px solid #2a2a2a; }
  .hang-hole {
    position: absolute; left: 145px; top: 38px;
    width: 116px; height: 25px; border-radius: 12px;
    background: var(--paper);
  }
  .splash {
    position: absolute; right: 0; top: 0; width: 170px; height: 180px;
    background: radial-gradient(circle at 62% 45%, var(--accent) 0%, var(--accent) 30%, rgba(247,220,0,0.5) 44%, rgba(247,220,0,0) 66%);
  }
  .brand-name {
    position: absolute; left: 36px; top: 88px;
    color: var(--paper); font-size: 29px; line-height: 32px; letter-spacing: 0.2px;
  }
  .strapline {
    position: absolute; left: 35px; top: 127px;
    color: var(--paper); font-size: 13px; line-height: 16px; letter-spacing: 0.2px;
    word-spacing: 6px;
  }
  .website {
    position: absolute; left: 80px; top: 155px;
    color: var(--paper); font-size: 13px; line-height: 16px;
  }

  .info-panel {
    position: absolute; left: 19px; top: 207px;
    width: 369px; height: 698px;
    background: var(--paper);
    padding: 12px 12px 0 12px;
    color: var(--text);
    font-size: 11.6px; line-height: 15.5px;
  }
  .standard-title { font-size: 16px; line-height: 20px; margin-bottom: 0; }
  .info-panel p { text-align: justify; margin-bottom: 15px; }
  .info-panel p b { font-weight: 700; }

  .markings-table {
    width: 338px; border-collapse: collapse;
    border: 1.5px solid var(--rule);
    font-size: 9.6px; margin-top: -1px;
  }
  .markings-table th {
    text-align: left; font-weight: 700; font-size: 10px;
    padding: 8px 6px; height: 31px; border-bottom: 1.5px solid var(--rule);
  }
  .markings-table th:first-child, .markings-table td:first-child { border-right: 1.5px solid var(--rule); width: 72px; }
  .markings-table td { padding: 3px 6px; height: 23.5px; }
  .markings-table tr:nth-child(2) td { padding-top: 10px; height: 30px; }
  .markings-table sup { font-size: 6px; }

  .warning { font-size: 8.8px; line-height: 12px; margin-top: 18px; }
  .warning b { font-weight: 700; }
  .tint-title { font-size: 8.8px; font-weight: 700; margin-top: 16px; margin-bottom: 1px; }
  .tint-list { font-size: 8.8px; line-height: 11.5px; }
  .tint-row { display: grid; grid-template-columns: 36px 72px 1fr; }
  .tint-row.wide { grid-template-columns: 36px 1fr; }

  .clear-window {
    position: absolute; left: 0; bottom: 0; width: 100%; height: 149px;
    background: linear-gradient(160deg, var(--silver-dark) 0%, var(--silver-light) 40%, #ffffff 55%, var(--silver-light) 70%, var(--silver-dark) 100%);
    border-top: 1px solid var(--ink);
  }
</style>
</head>
<body>
<div class="canvas">
  <div class="bag">
    <div class="header">
      <div class="splash" role="img" aria-label="Yellow paint splash decoration"></div>
      <div class="hang-hole"></div>
      <div class="brand-name">kerMosafety</div>
      <div class="strapline">COMFORT | STYLE | PROTECTION</div>
      <div class="website">www.kerMosafety.com</div>
    </div>

    <div class="info-panel">
      <div class="standard-title">EN166:2001</div>
      <p><b>Taking care of your safety eyewear:</b> Store at normal room temperature in a box or locker. Transport in the box, bag or case provided and not unprotected with other items. Clean with warm soapy water, rinse then dry with a clean lint free cloth or tissue. Disinfect when required with mild household or medical disinfectant, then rinse off and dry as in previous clause. Check daily; hinge screws, pivots or other moving parts for tightness and security. Broken products, scratched lenses and items obviously at the end of their useful life must be immediately replaced.</p>
      <p><b>Product Life:</b> If stored in good condition at an even ambient temperature they will last in excess of 2 years but must be thoroughly inspected before use. If there are any signs of deterioration they should be replaced.</p>
      <p><b>Product Markings:</b> If the symbols S, F or B are not common to both ocular and the frame, then it is the lower level that shall be assigned to the complete eye protector.</p>

      <table class="markings-table">
        <tr><th>SYMBOL</th><th>DESCRIPTION OF THE FIELD OF USE/MARKINGS</th></tr>
        <tr><td>No symbol</td><td>General purpose, low speed impacts (frame only)</td></tr>
        <tr><td>S</td><td>Increased robustness</td></tr>
        <tr><td>F</td><td>High speed particles, Low energy impact <sup>1,2</sup></td></tr>
        <tr><td>B</td><td>High speed particles, Medium energy impact <sup>1,2</sup></td></tr>
        <tr><td>1</td><td>Optical class 1</td></tr>
        <tr><td>EN166</td><td>European standard number for Personal Eye Protection</td></tr>
      </table>

      <div class="warning"><b>Warning:</b> <sup>1</sup>Impacts may be transmitted to eyewear worn underneath, thus creating a hazard. <sup>2</sup>Applicable at room temperature only unless marked with the letter T. Should the product cause skin irritation its use should be discontinued and medical advice sought.</div>

      <div class="tint-title">Additional markings for tinted lenses</div>
      <div class="tint-list">
        <div class="tint-row wide"><span>EN169</span><span>Welding shades are identified by shade density number prior to manufacturer's identification.</span></div>
        <div class="tint-row"><span>EN170</span><span>Ultra Violet filters</span><span>2 or 3 precedes the shade code for ultra violet filters</span></div>
        <div class="tint-row"><span>EN171</span><span>Infrared filters</span><span>4 precedes the shade code for infrared filters</span></div>
        <div class="tint-row"><span>EN172</span><span>Sun glare filters</span><span>5 or 6 precedes the shade code for sun filters</span></div>
      </div>
    </div>

    <div class="clear-window" role="img" aria-label="Clear vision panel"></div>
  </div>
</div>
</body>
</html>
```